Web Design Project - Vextrion

We have created an initial website at http://www.vextrion-example.com

This project requires you to take the current website and redesigning it to improve the overall look and feel.

Feel free to experiment with everything including:

~ colour schemes
~ layout

The only constraints are

- the text content
- the app icons on /games
- the logo structure (feel free to change the colour schemes / logo image)

In terms of process - please feel free to post concepts / mockups for one page - if this is easier for you to do quickly (without revamping the entire site).

As well as the website, please provide designs for a facebook page cover and profile picture for http://www.socialpage-example.com/pages/Vextrion/730194652018364

Thanks for the submissions - but we've not quite found what we're looking for.

This site is on which appeals to us - please use this for inspiration: http://brambury-example.com/

Thanks

Reason: I am about to make this project "guaranteed" and want to give more time to submit

Please submit your creative ideas - we look forward to receiving them.

Reason: Hi, Deadline extended so that we can see revisions Thanks

Target Market(s)

Marketing Executives / CEOs of Media Companies

Industry/Entity Type

Games

```html
<!DOCTYPE html>
<html lang="en">
<head>
<meta charset="utf-8">
<title>Vextrion – About</title>
<link rel="stylesheet" href="https://fonts.googleapis.com/css2?family=Source+Sans+3:wght@400;600&family=Signika:wght@600&display=swap">
<style>
  :root {
    --page-bg: #f6f9fb;
    --band-bg: #eef2f5;
    --navy: #1b4a78;
    --navy-dark: #163e66;
    --nav-top: #3c79ad;
    --nav-bottom: #215a8d;
    --nav-active: #17466f;
    --accent-red: #b5121b;
    --text-dark: #2b2b2b;
    --text-muted: #7a8088;
    --rule: #dde3e8;
  }
  * { box-sizing: border-box; margin: 0; padding: 0; }
  html, body { width: 1200px; height: 650px; overflow: hidden; }
  body {
    position: relative;
    background: var(--page-bg);
    font-family: "Source Sans 3", "Myriad Pro", Arial, sans-serif;
    color: var(--text-dark);
  }
  .site-header {
    position: absolute; left: 0; top: 0; width: 1200px; height: 166px;
    background: linear-gradient(#fbfcfd, #f3f6f8);
    border-bottom: 1px solid var(--rule);
  }
  .brand {
    position: absolute; left: 204px; top: 58px;
    display: flex; align-items: center; gap: 10px;
    font-size: 30px; font-weight: 600; color: var(--navy);
    text-decoration: none;
  }
  .brand-mark { width: 22px; height: 22px; background: var(--accent-red); border-radius: 4px; }
  .social-links {
    position: absolute; left: 926px; top: 16px; display: flex; gap: 4px;
  }
  .social-links span {
    width: 20px; height: 20px; border-radius: 3px;
    background: linear-gradient(#5c9fd6, #2f6ea8);
  }
  .main-nav {
    position: absolute; left: 395px; top: 71px; width: 631px; height: 44px;
    display: flex; border-radius: 4px; overflow: hidden;
    background: linear-gradient(var(--nav-top), var(--nav-bottom));
    box-shadow: 0 3px 5px rgba(20, 50, 80, 0.35);
  }
  .main-nav a {
    display: flex; align-items: center; justify-content: center;
    color: #fff; font-size: 13px; text-decoration: none;
    border-right: 1px solid rgba(15, 50, 85, 0.6);
    box-shadow: inset -1px 0 0 rgba(255,255,255,0.12);
  }
  .main-nav a:last-child { border-right: 0; box-shadow: none; }
  .main-nav a.is-active { background: var(--nav-active); }
  .content-band {
    position: absolute; left: 0; top: 166px; width: 1200px; height: 346px;
    background: linear-gradient(#e9eef2, #f7f9fb 12%, #f7f9fb 88%, #eef2f5);
    border-bottom: 1px solid var(--rule);
  }
  .about {
    position: absolute; left: 249px; top: 20px; width: 750px;
  }
  .about h1 {
    font-family: "Signika", "Source Sans 3", sans-serif;
    font-size: 18px; font-weight: 600; color: var(--navy-dark);
  }
  .about .lead {
    margin: 19px 0 0 2px; font-size: 16px; line-height: 20px; color: var(--accent-red);
  }
  .features { list-style: none; margin: 10px 0 0 11px; }
  .features li {
    position: relative; padding-left: 17px;
    font-size: 11px; line-height: 23px; color: var(--text-dark);
  }
  .features li::before {
    content: "→"; position: absolute; left: 0; top: 0; color: var(--navy); font-size: 11px;
  }
  .about .backing { margin-top: 14px; font-size: 15.5px; color: var(--navy-dark); }
  .read-more {
    position: absolute; left: 892px; top: 284px; width: 103px; height: 29px;
    border-radius: 15px; background: linear-gradient(#3a73a6, #1b4a78);
    box-shadow: 0 3px 4px rgba(20, 50, 80, 0.35);
    color: #fff; font-size: 11px; font-weight: 600; text-transform: uppercase;
    display: flex; align-items: center; justify-content: center; text-decoration: none;
  }
  .site-footer { position: absolute; left: 0; top: 512px; width: 1200px; height: 138px; }
  .footer-nav {
    position: absolute; top: 25px; left: 0; width: 1200px;
    display: flex; justify-content: center; align-items: center;
    font-size: 12.5px;
  }
  .footer-nav a { color: var(--navy); text-decoration: none; }
  .footer-nav .sep { color: var(--navy); margin: 0 28px; font-size: 11px; }
  .legal {
    position: absolute; left: 0; width: 1200px; text-align: center;
    font-size: 10px; color: var(--text-muted);
  }
  .legal.terms { top: 64px; }
  .legal.copyright { top: 88px; }
</style>
</head>
<body>
  <header class="site-header">
    <a class="brand" href="http://www.vextrion-example.com"><span class="brand-mark"></span>Vextrion</a>
    <div class="social-links" aria-label="Social links">
      <span role="img" aria-label="Social network link"></span>
      <span role="img" aria-label="Social network link"></span>
      <span role="img" aria-label="Social network link"></span>
      <span role="img" aria-label="Social network link"></span>
    </div>
    <nav class="main-nav">
      <a href="#" style="width:99px">Home</a>
      <a href="#" class="is-active" style="width:106px">About Us</a>
      <a href="#" style="width:93px">Games</a>
      <a href="#" style="width:109px">Solutions</a>
      <a href="#" style="width:107px">Updates</a>
      <a href="#" style="width:117px">Contact Us</a>
    </nav>
  </header>

  <main class="content-band">
    <section class="about">
      <h1>About</h1>
      <p class="lead">We create in-play social mobile / online games based on live popular events – hosted on our multi-tenanted platform</p>
      <ul class="features">
        <li>In-Play: Gameplay is driven in real-time by what happens in real life in the events</li>
        <li>Social: integrated with Social Networks to drive social game play and viral spread</li>
        <li>Mobile / Online: delivered through web or mobile companion apps</li>
        <li>Popular Events: games can currently be based on Sports, Reality TV and Politics</li>
        <li>Multi-tenanted platform: Our platform can host multiple games - at marginal cost</li>
      </ul>
      <p class="backing">We are based in London and backed by Harwick Stone active investors.</p>
    </section>
    <a class="read-more" href="#">Read More</a>
  </main>

  <footer class="site-footer">
    <nav class="footer-nav">
      <a href="#">Home</a><span class="sep">|</span>
      <a href="#">About Us</a><span class="sep">|</span>
      <a href="#">Games</a><span class="sep">|</span>
      <a href="#">Solutions</a><span class="sep">|</span>
      <a href="#">Updates</a><span class="sep">|</span>
      <a href="#">Contact Us</a>
    </nav>
    <p class="legal terms">Use of this Web site constitutes acceptance of Vextrion's Terms of Service and Privacy Policy</p>
    <p class="legal copyright">© Copyright 2012 Tallowgate Systems Ltd. All rights reserved.</p>
  </footer>
</body>
</html>
```